Cozy Sprouts Business Cards

I need a business card for my new Company called Cozy Sprouts. We create handmade baby moccasins, headbands, t-shirts and more. I want some that will appeal to parents, and to go with the colors of my logo that I have attached. feel free to be creative. I would like my logo placed somewhere on the card.

Industry/Entity Type

Retail

Contact Information for Business Card

Cozy Sprouts
24816 Maplecrest D #5172
Larkvale Wr 92738
Rosalind Vantrey Ceo
Info@Cozy-Sprouts.com
www.Cozy-Sprouts.com
Phone 9495817320

Requirements
Nice to have
• Logo included

```html
<!DOCTYPE html>
<html lang="en">
<head>
<meta charset="utf-8">
<title>Cozy Sprouts – Business Card</title>
<link rel="stylesheet" href="https://fonts.googleapis.com/css2?family=Comic+Neue:wght@400;700&family=Oswald:wght@400;500&display=swap">
<style>
  :root {
    --page-bg: #ece8e4;
    --card-bg: #f7f5f2;
    --ink: #4f4f4f;
    --brand-dark: #2b2b2b;
    --accent: #f08a4b;
    --band-light: #eaa07a;
    --band-dark: #d67f55;
  }
  * { box-sizing: border-box; margin: 0; padding: 0; }
  html, body {
    width: 1200px; height: 970px; overflow: hidden;
    background: var(--page-bg);
  }
  .business-card {
    position: absolute; left: 105px; top: 210px;
    width: 990px; height: 550px;
    background: var(--card-bg);
    box-shadow: 0 10px 30px rgba(0,0,0,.18);
    overflow: hidden;
  }
  .wave-band { position: absolute; left: 0; top: 0; width: 990px; height: 550px; }
  .brand {
    position: absolute; left: 56px; top: 182px; width: 395px;
    display: flex; flex-direction: column; align-items: center; gap: 30px;
  }
  .brand-mark {
    width: 80px; height: 80px; background: var(--accent);
    transform: rotate(45deg); border-radius: 6px;
  }
  .brand-name {
    font-family: "Comic Neue", sans-serif; font-weight: 700;
    font-size: 56px; line-height: 1; color: var(--brand-dark); white-space: nowrap;
  }
  .divider {
    position: absolute; left: 474px; top: 160px;
    width: 3px; height: 225px; background: var(--accent);
  }
  .contact {
    position: absolute; left: 496px; top: 168px;
    font-family: "Oswald", sans-serif; color: var(--ink);
  }
  .contact-name { font-size: 42px; font-weight: 500; letter-spacing: .6px; line-height: 1.1; }
  .contact-role { font-size: 24px; font-weight: 500; color: var(--accent); line-height: 1.2; margin-bottom: 6px; }
  .contact-list { list-style: none; }
  .contact-item {
    display: flex; align-items: center; gap: 12px;
    font-size: 24px; font-weight: 500; letter-spacing: .3px; line-height: 44px;
    white-space: nowrap;
  }
  .contact-item svg { width: 18px; height: 18px; fill: var(--accent); flex: none; }
</style>
</head>
<body>
  <article class="business-card">
    <svg class="wave-band" viewBox="0 0 990 550" aria-hidden="true">
      <defs>
        <linearGradient id="bandFill" x1="0" y1="0" x2="0" y2="1">
          <stop offset="0" stop-color="var(--band-light)"/>
          <stop offset="1" stop-color="var(--band-dark)"/>
        </linearGradient>
      </defs>
      <path d="M0 480 C90 505 170 522 260 518 C420 508 560 445 727 440 C840 437 930 462 990 486 L990 550 L0 550 Z" fill="url(#bandFill)" opacity=".9"/>
    </svg>

    <div class="brand">
      <div class="brand-mark"></div>
      <div class="brand-name">Cozy Sprouts</div>
    </div>

    <div class="divider"></div>

    <div class="contact">
      <h1 class="contact-name">Rosalind Vantrey</h1>
      <p class="contact-role">CEO</p>
      <ul class="contact-list">
        <li class="contact-item">
          <svg viewBox="0 0 24 24"><path d="M12 2a7 7 0 0 0-7 7c0 5 7 13 7 13s7-8 7-13a7 7 0 0 0-7-7zm0 9.5A2.5 2.5 0 1 1 12 6.5a2.5 2.5 0 0 1 0 5z"/></svg>
          24816 Maplecrest D #5172 Larkvale Wr 92738
        </li>
        <li class="contact-item">
          <svg viewBox="0 0 24 24"><path d="M2 5h20v14H2z"/><path d="M3 6l9 7 9-7" fill="none" stroke="var(--card-bg)" stroke-width="1.6"/></svg>
          Info@Cozy-Sprouts.com
        </li>
        <li class="contact-item">
          <svg viewBox="0 0 24 24"><circle cx="12" cy="12" r="10"/><path d="M2 12h20M12 2c3 3 3 17 0 20M12 2c-3 3-3 17 0 20" fill="none" stroke="var(--card-bg)" stroke-width="1.5"/></svg>
          www.Cozy-Sprouts.com
        </li>
      </ul>
    </div>
  </article>
</body>
</html>
```